Pebble Reach ~ Business Card Design Project

Pebble Reach is a digital marketing agency which creates and maintains online social presence for brands and businesses. Services include monthly stream management, social media advertising campaigns, online press release distribution, search engine optimization, copywriting, digital strategy consultation, video marketing campaigns, fan acquisition, and Wordpress website development.
The company is currently rebranding to a full service agency from just a social media firm, with a new website launching soon. I'm looking for an extremely creative and modern business card design that pops out from the rest and fits with our company's sector/services.
It will need to be 1039 x 697 pixels, and rectangular (not rounded edges or corners). Utilize our company logo (file is attached), and include the following information in any design or layout:
Mark Telford
CEO/Creative Director
Pebble Reach
Facebook: facebook.com/pebblereach
Twitter: @PebbleReach
Phone: +1 555 014 8832
Cell: +1 555 016 4907
Email: mark@pebblereach.example
Website: www.pebblereach.example
318 Birchmore Avenue, Suite 207
Windsor, ON
K7Z 4X8

```html
<!DOCTYPE html>
<html lang="en">
<head>
<meta charset="utf-8">
<title>Pebble Reach — Business Cards</title>
<link rel="stylesheet" href="https://fonts.googleapis.com/css2?family=Arimo:wght@400;700&display=swap">
<style>
  :root {
    --backdrop: #d9dadc;
    --card-white: #ffffff;
    --card-mist: #eceef3;
    --brand-blue: #2b4ea8;
    --brand-blue-deep: #1f4fb0;
    --brand-cyan: #22a6e6;
    --brand-red: #d4202a;
    --brand-orange: #f0642a;
    --ink-light: #ffffff;
    --label-red: #e2383a;
    --shadow: rgba(0, 0, 0, 0.22);
  }
  * { box-sizing: border-box; margin: 0; padding: 0; }
  html, body {
    width: 1067px;
    height: 1200px;
    overflow: hidden;
    background: var(--backdrop);
    font-family: "Arimo", Arial, sans-serif;
  }
  .sheet {
    position: relative;
    width: 1067px;
    height: 1200px;
  }
  .card {
    position: absolute;
    left: 183px;
    width: 700px;
    height: 470px;
    overflow: hidden;
    box-shadow: 0 10px 28px var(--shadow);
  }
  .card--front { top: 70px; background: var(--card-white); }
  .card--back  { top: 650px; background: linear-gradient(135deg, var(--card-white) 40%, var(--card-mist)); }

  /* front */
  .front__top {
    position: absolute; inset: 0 0 230px 0;
    background: radial-gradient(ellipse at 80% 40%, var(--card-mist) 0%, var(--card-white) 70%);
  }
  .brand {
    position: absolute; left: 44px; top: 84px;
    display: flex; align-items: center; gap: 18px;
  }
  .brand__dot {
    width: 62px; height: 62px; border-radius: 50%;
    background: var(--brand-blue);
  }
  .brand__name {
    font-size: 50px; font-weight: 400; letter-spacing: -1px;
    color: var(--brand-blue);
  }
  .front__stripe {
    position: absolute; left: 0; top: 240px; width: 100%; height: 22px;
  }
  .front__panel {
    position: absolute; left: 0; top: 262px; width: 100%; height: 208px;
    background: radial-gradient(ellipse at 55% 20%, var(--brand-cyan) 0%, var(--brand-blue-deep) 85%);
    color: var(--ink-light);
  }
  .person {
    position: absolute; left: 50px; top: 36px;
    font-size: 15px; line-height: 1.2;
  }
  .person__name {
    font-size: 23px; font-weight: 700; color: var(--brand-red);
    margin-bottom: 2px;
  }
  .address {
    position: absolute; left: 270px; top: 40px;
    font-size: 15px; line-height: 1.3;
  }
  .contacts {
    position: absolute; left: 50px; top: 132px;
    display: grid; grid-template-columns: 210px 230px 230px;
    row-gap: 4px; font-size: 15px;
  }
  .contacts__label { color: var(--label-red); margin-right: 6px; }

  /* back */
  .back__band { position: absolute; inset: 0; width: 100%; height: 100%; }
  .back__name {
    position: absolute; right: 70px; top: 150px;
    font-size: 74px; font-weight: 400; line-height: 0.95;
    letter-spacing: -2px; color: var(--brand-blue);
    text-align: left;
  }
</style>
</head>
<body>
<main class="sheet">

  <section class="card card--front" aria-label="Business card front">
    <div class="front__top"></div>
    <div class="brand">
      <span class="brand__dot"></span>
      <span class="brand__name">Pebble Reach</span>
    </div>
    <svg class="front__stripe" viewBox="0 0 700 40" preserveAspectRatio="none" style="height:40px">
      <defs>
        <linearGradient id="stripe-fill" x1="0" x2="1">
          <stop offset="0" stop-color="#c3161f"/>
          <stop offset="1" stop-color="#f05a28"/>
        </linearGradient>
      </defs>
      <path d="M0 0 H700 V22 H92 L80 36 L68 22 H0 Z" fill="url(#stripe-fill)"/>
    </svg>
    <div class="front__panel">
      <div class="person">
        <p class="person__name">Mark Telford</p>
        <p>CEO/Creative Director</p>
        <p>Pebble Reach</p>
      </div>
      <div class="address">
        <p>318 Birchmore Avenue, Suite 207</p>
        <p>Windsor, ON</p>
        <p>K7Z 4X8</p>
      </div>
      <div class="contacts">
        <p><span class="contacts__label">p:</span>+1 555 014 8832</p>
        <p><span class="contacts__label">e:</span>mark@pebblereach.example</p>
        <p><span class="contacts__label">f:</span>facebook.com/pebblereach</p>
        <p><span class="contacts__label">c:</span>+1 555 016 4907</p>
        <p><span class="contacts__label">w:</span>www.pebblereach.example</p>
        <p><span class="contacts__label">t:</span>@PebbleReach</p>
      </div>
    </div>
  </section>

  <section class="card card--back" aria-label="Business card back">
    <svg class="back__band" viewBox="0 0 700 470" preserveAspectRatio="none">
      <defs>
        <linearGradient id="band-fill" x1="0" y1="0" x2="1" y2="1">
          <stop offset="0" stop-color="#d01c24"/>
          <stop offset="1" stop-color="#f26a2a"/>
        </linearGradient>
      </defs>
      <path d="M0 0 H250 L440 470 H0 Z" fill="url(#band-fill)"/>
    </svg>
    <p class="back__name">Pebble<br>Reach</p>
  </section>

</main>
</body>
</html>
```